Aircraft maintenance buisness card

I am an aircraft mechanic looking for a personal buisness card . I would like my name and a title of Aircraft Maintenance Manager . I would like a suttle picture of an aircraft and helicopter .

elegant and professional wtih my contact .

My name should be on the car and Aircraft Maintenance Manager under with my contact infor below .

i have attached some pictures but i am open to other pics and ideas . I would like a airliner or private jet and a helicopter in the picture . The Images should be suttle and not the main idea . I also uploaded a picture of a jet engine which is cool . Be creative and i will work with you to finalize something .
Updates

Project Deadline Extended
Reason: Looking for more variations . Very good so far but looiking for a bit more styles and i uploaded my logo that i purchased . Please use my logo and be creative with it . I like some variations of black card with maybe some pictures that i uploaded but i am open to ideas . Be creative and i will work with you .

Project Deadline Extended
Reason: Looking for more designs and variations . Not yet satisfied with the designs i have gotten .

Industry/Entity Type

Aviation

Contact Information for Business Card

Aircraft Maintenance Manager

Font styles to use
Serif

Colors

Designer to choose colors to be used in the design.

Requirements
Must have
• An aviation related Logo if possible incorporated in the card possibly
• My name
• Tiberio Malvade Furtunato
• 482 Pellow St.
• Halverton , PA
• 08519
• Email: Lwskyfixtech@mailvora.com
Nice to have
• Suttle Backround of a Private Jet or Airliner and a Helicopter .

```html
<!DOCTYPE html>
<html lang="en">
<head>
<meta charset="utf-8">
<title>Malvade Aero – Business Card</title>
<link rel="stylesheet" href="https://fonts.googleapis.com/css2?family=Libre+Baskerville:wght@700&family=Questrial&display=swap">
<style>
  :root {
    --backdrop: #8f9094;
    --card-white: #ffffff;
    --brand-blue: #1d4aa0;
    --ink: #2a2a2a;
  }
  * { box-sizing: border-box; margin: 0; padding: 0; }
  html, body { width: 1200px; height: 1080px; overflow: hidden; }
  body {
    background: var(--backdrop);
    font-family: "Questrial", "Helvetica Neue", sans-serif;
    position: relative;
  }
  .card {
    position: absolute;
    left: 220px;
    width: 760px;
    height: 430px;
    background: var(--card-white);
    box-shadow: 0 6px 18px rgba(0,0,0,.25);
    overflow: hidden;
  }
  .card--front { top: 80px; }
  .card--back { top: 560px; }

  .collage {
    position: absolute; inset: 0;
    display: grid;
    grid-template-columns: 1fr 1fr 1fr;
    grid-template-rows: 1fr 1fr;
  }
  .collage__tile { width: 100%; height: 100%; }
  .tile--red-heli { background: linear-gradient(160deg, #a8b3c2 0%, #c7a6a2 55%, #b9bec7 100%); }
  .tile--airliner { background: linear-gradient(180deg, #e6e9ee 0%, #d3d8df 100%); }
  .tile--showroom-heli { background: linear-gradient(160deg, #a7a59f 0%, #cfcdc8 55%, #bdb3a6 100%); }
  .tile--airliner-flight { background: linear-gradient(180deg, #9fb6c8 0%, #7f9aa8 60%, #8ea79e 100%); }
  .tile--blue-heli { background: linear-gradient(160deg, #9a9c9e 0%, #b3b8c2 50%, #8f939a 100%); }
  .tile--black-heli { background: linear-gradient(180deg, #b7c5d4 0%, #9eabb3 55%, #8f9c8d 100%); }

  .collage__veil {
    position: absolute; inset: 0;
    background: rgba(255,255,255,.28);
  }
  .brand {
    position: absolute;
    display: flex; align-items: center; gap: 14px;
    color: var(--brand-blue);
    font-family: "Questrial", sans-serif;
    white-space: nowrap;
  }
  .brand__dot {
    border-radius: 50%;
    background: var(--brand-blue);
    flex: none;
  }
  .card--front .brand {
    left: 50%; top: 50%;
    transform: translate(-50%, -50%);
    font-size: 46px;
    background: rgba(255,255,255,.82);
    padding: 16px 30px;
  }
  .card--front .brand__dot { width: 40px; height: 40px; }
  .card--back .brand {
    left: 60px; top: 180px;
    font-size: 26px;
  }
  .card--back .brand__dot { width: 26px; height: 26px; }

  .contact {
    position: absolute;
    left: 330px; top: 96px;
    color: var(--ink);
  }
  .contact__name {
    font-family: "Libre Baskerville", Georgia, serif;
    font-weight: 700;
    font-size: 27px;
    color: var(--brand-blue);
    letter-spacing: .2px;
  }
  .contact__title {
    font-size: 19px;
    margin-top: 6px;
    letter-spacing: .4px;
  }
  .contact__address {
    font-style: normal;
    font-size: 19px;
    line-height: 1.3;
    margin-top: 42px;
    letter-spacing: .3px;
  }
  .contact__email {
    display: flex; align-items: center; gap: 10px;
    font-size: 19px;
    margin-top: 24px;
    letter-spacing: .3px;
  }
  .contact__icon { width: 26px; height: 26px; flex: none; }
</style>
</head>
<body>

  <section class="card card--front" aria-label="Card front">
    <div class="collage">
      <div class="collage__tile tile--red-heli" role="img" aria-label="Photo of a red helicopter landing on a helipad"></div>
      <div class="collage__tile tile--airliner" role="img" aria-label="Photo of a white airliner nose at a hangar"></div>
      <div class="collage__tile tile--showroom-heli" role="img" aria-label="Photo of a silver helicopter on an exhibition floor"></div>
      <div class="collage__tile tile--airliner-flight" role="img" aria-label="Photo of a blue and white airliner flying over green hills"></div>
      <div class="collage__tile tile--blue-heli" role="img" aria-label="Photo of a blue and white helicopter near a rock face"></div>
      <div class="collage__tile tile--black-heli" role="img" aria-label="Photo of a black helicopter hovering above a city"></div>
    </div>
    <div class="collage__veil"></div>
    <div class="brand">
      <span class="brand__dot"></span>
      <span class="brand__name">Malvade Aero</span>
    </div>
  </section>

  <section class="card card--back" aria-label="Card back">
    <div class="brand">
      <span class="brand__dot"></span>
      <span class="brand__name">Malvade Aero</span>
    </div>
    <div class="contact">
      <h1 class="contact__name">Tiberio Malvade Furtunato</h1>
      <p class="contact__title">Aircraft Maintenance Manager</p>
      <address class="contact__address">
        482 Pellow St.<br>
        Halverton , PA, 08519
      </address>
      <p class="contact__email">
        <svg class="contact__icon" viewBox="0 0 26 26" aria-hidden="true">
          <circle cx="13" cy="13" r="13" fill="var(--brand-blue)"/>
          <rect x="7" y="9" width="12" height="8" fill="#fff"/>
          <path d="M7 9 L13 14 L19 9" fill="none" stroke="var(--brand-blue)" stroke-width="1.2"/>
        </svg>
        <span>Lwskyfixtech@mailvora.com</span>
      </p>
    </div>
  </section>

</body>
</html>
```